Custom Apparel Decorating Company needs a Website Home Page Banner Design

We are in need of a website Home page banner design for a small company based in Canada called Quelvana. We are a custom apparel company that offers custom apparel (t-shirts, hoodies, hats etc) to Companies, Organizations/groups, bands, Spirit wear and individuals. We would like the design to match with the logo files we have attached to the campaign. The Website has not been created yet planning to tie the website into the home page banner for flow. Thinking of using Duda or Shopify for the website if that helps! We are really looking forward to seeing the designs.

Target Market(s)

Companies, Organizations/Groups, Bands, Spirit wear and Individuals. Anyone that is looking to have there company or own logo/Design put on a piece of clothing.

Requirements
Must have
• -Colours in the logo files.
• -FUN creating the Home Page Banner!!! :)
Nice to have
• -Up Beat feel to it (it's the first image you will see when you go to the website, it's the store front so we want to grab the attention of the potential customers)

```html
<!DOCTYPE html>
<html lang="en">
<head>
<meta charset="utf-8">
<title>Quelvana Apparel – Home Banner</title>
<link rel="stylesheet" href="https://fonts.googleapis.com/css2?family=Cinzel:wght@400;600&family=Permanent+Marker&display=swap">
<style>
  :root {
    --navy: #344a63;
    --blush: #fdcbca;
    --headline-pink: #f7c3bf;
    --ivory: #f4efe9;
    --brand-blue: #4a78c4;
    --photo-hat-a: #d9cbbf;
    --photo-hat-b: #a47f6c;
    --photo-hoodie-a: #e4e4e6;
    --photo-hoodie-b: #2a2a2e;
    --photo-tee-a: #c9cdd3;
    --photo-tee-b: #3d4d6c;
    --frame-white: #ffffff;
  }
  * { box-sizing: border-box; margin: 0; padding: 0; }
  html, body { width: 1200px; height: 578px; overflow: hidden; }
  .banner {
    position: relative;
    width: 1200px;
    height: 578px;
    background: var(--blush);
    overflow: hidden;
    font-family: "Cinzel", serif;
  }
  .banner__panel {
    position: absolute;
    left: 0; top: 0;
    width: 598px; height: 578px;
    background: var(--navy);
  }
  .headline {
    position: absolute;
    left: 27px; top: 86px;
    font-family: "Permanent Marker", cursive;
    font-size: 49px;
    letter-spacing: 3px;
    color: var(--headline-pink);
    white-space: nowrap;
  }
  .audience-list {
    position: absolute;
    left: 44px; top: 163px;
    list-style: none;
  }
  .audience-list li {
    position: relative;
    padding-left: 27px;
    height: 46.3px;
    font-size: 27px;
    letter-spacing: 2.5px;
    color: var(--ivory);
    white-space: nowrap;
  }
  .audience-list li::before {
    content: "";
    position: absolute;
    left: 5px; top: 16px;
    width: 7px; height: 7px;
    border-radius: 50%;
    background: var(--ivory);
  }
  .brand {
    position: absolute;
    left: 602px; top: 14px;
    width: 200px;
    text-align: center;
  }
  .brand__mark {
    display: block;
    width: 30px; height: 30px;
    margin: 0 auto 8px;
    background: var(--brand-blue);
  }
  .brand__name {
    font-family: "Cinzel", serif;
    font-weight: 600;
    font-size: 19px;
    letter-spacing: 1px;
    color: var(--brand-blue);
    white-space: nowrap;
  }
  .frame-corner {
    position: absolute;
    left: 804px; top: 78px;
    width: 100px; height: 84px;
    background: var(--navy);
  }
  .photo {
    position: absolute;
  }
  .photo--hat {
    left: 815px; top: 89px;
    width: 276px; height: 413px;
    background: linear-gradient(160deg, var(--photo-hat-a) 0%, #c9a892 55%, var(--photo-hat-b) 100%);
  }
  .photo-frame--tee {
    position: absolute;
    left: 367px; top: 345px;
    width: 322px; height: 233px;
    background: var(--frame-white);
  }
  .photo--tee {
    left: 376px; top: 353px;
    width: 312px; height: 225px;
    background: radial-gradient(ellipse at 55% 70%, var(--photo-tee-b) 0%, #6a7690 45%, var(--photo-tee-a) 80%);
  }
  .photo--hoodies {
    left: 580px; top: 287px;
    width: 313px; height: 210px;
    border: 7px solid var(--frame-white);
    border-left-width: 0;
    background: radial-gradient(ellipse at 50% 75%, var(--photo-hoodie-b) 0%, #4a4a50 50%, var(--photo-hoodie-a) 85%);
  }
  .tag {
    position: absolute;
    height: 40px;
    border-radius: 20px 6px 22px 4px;
    display: flex;
    align-items: center;
    justify-content: center;
    font-family: "Cinzel", serif;
    font-size: 17px;
    letter-spacing: 1px;
  }
  .tag--hats {
    left: 955px; top: 82px;
    width: 190px;
    transform: rotate(33deg);
    background: var(--navy);
    color: var(--ivory);
  }
  .tag--hoodies {
    left: 790px; top: 478px;
    width: 185px;
    transform: rotate(-38deg);
    background: var(--ivory);
    color: var(--navy);
  }
  .tag--tees {
    left: 283px; top: 518px;
    width: 190px;
    transform: rotate(40deg);
    background: var(--ivory);
    color: var(--navy);
  }
</style>
</head>
<body>
<main class="banner">
  <section class="banner__panel">
    <h1 class="headline">REMEMBER US FOR</h1>
    <ul class="audience-list">
      <li>Corporate Orders</li>
      <li>Groups Purchase</li>
      <li>Band Performance,</li>
      <li>Spirit wear</li>
      <li>individuals</li>
    </ul>
  </section>

  <div class="brand">
    <span class="brand__mark"></span>
    <div class="brand__name">Quelvana Apparel</div>
  </div>

  <div class="frame-corner"></div>
  <div class="photo photo--hat" role="img" aria-label="Woman wearing a wide-brimmed crocheted sun hat"></div>
  <div class="tag tag--hats">Hats</div>

  <div class="photo-frame--tee"></div>
  <div class="photo photo--tee" role="img" aria-label="Man wearing a navy long-sleeve printed shirt"></div>
  <div class="photo photo--hoodies" role="img" aria-label="Two people wearing black printed hoodies"></div>

  <div class="tag tag--hoodies">Hoodies</div>
  <div class="tag tag--tees">T-shirts</div>
</main>
</body>
</html>
```